Business Card Design Project

This design is a slimline business card 45mm x90mm, the card will be printed at 49mm x 94mm and cut to 45mm x90 mm, this needs to be considered in the design. The content required on the front and back of the business card is attached in a pdf; the design will be done using photo shop as we use CS6 in our business. The design needs to be developed using a CMYK colour pallet, the main colours used on our business are red, grey black and white. A snapshot of our business brochure and new website has been provided to give you an understanding on our businesses look and feel.
FRONT OF BUSINESS CARD
Director
Marcus Feld
Ph+61 0421780213
www.brightvanecontracting.com.au
marcusfeld@brightvanecontracting.com.au
BACK OF BUSINESS CARD
SUPPORTING CLIENTS IN
Oil & Gas I Minerals & Metals I Petrochemical I Manufacturing
Building & Construction I Telecommunication I Rail I Civil I New Industries
KNOWLEDGE I EXPERTISE I EXPERIENCE I CAPACITY

```html
<!DOCTYPE html>
<html lang="en">
<head>
<meta charset="utf-8">
<title>Brightvane Contracting – Business Cards</title>
<link rel="stylesheet" href="https://fonts.googleapis.com/css2?family=Mulish:wght@400;600;800;900&display=swap">
<style>
  :root {
    --bg: #c9c9c9;
    --black: #0c0c0c;
    --black-soft: #2a2a2a;
    --red: #e0202e;
    --red-dark: #c2151f;
    --white: #ffffff;
    --paper: #f4f4f4;
    --ink: #1b1b1b;
    --grey-light: #bdbdbd;
  }
  * { box-sizing: border-box; margin: 0; padding: 0; }
  html, body {
    width: 1200px; height: 1023px; overflow: hidden;
    background: var(--bg);
    font-family: "Mulish", Arial, sans-serif;
  }
  .card {
    position: absolute;
    width: 620px; height: 310px;
    box-shadow: 0 8px 24px rgba(0,0,0,.25);
    overflow: hidden;
  }

  /* Back of card (black) */
  .card--back {
    left: 70px; top: 110px;
    background: linear-gradient(160deg, var(--black-soft) 0%, var(--black) 45%, #000 100%);
    color: var(--white);
  }
  .back-brand { position: absolute; left: 40px; top: 150px; }
  .brand-name {
    display: flex; align-items: center; gap: 10px;
    font-weight: 900; font-size: 26px; letter-spacing: .5px; text-transform: uppercase;
    line-height: 1;
  }
  .brand-mark { width: 14px; height: 14px; background: var(--red); flex: none; }
  .brand-tagline {
    margin-top: 6px; margin-left: 24px;
    font-size: 9.5px; font-weight: 600; letter-spacing: .2px;
  }
  .web-band {
    position: absolute; right: 0; top: 70px;
    width: 250px; height: 80px;
    background: linear-gradient(90deg, var(--red-dark), var(--red));
    display: flex; align-items: center; justify-content: center;
  }
  .web-band .web { color: var(--white); font-size: 12.5px; font-weight: 600; letter-spacing: .2px; }
  .sectors {
    position: absolute; left: 40px; right: 40px; bottom: 22px;
    font-size: 9px; line-height: 1.5; color: var(--grey-light);
  }
  .sectors-heading { color: var(--red); font-weight: 800; letter-spacing: .6px; }
  .capabilities { margin-top: 4px; color: var(--white); font-weight: 800; letter-spacing: 1px; }

  /* Front of card (white) */
  .card--front {
    left: 510px; top: 500px;
    background: linear-gradient(180deg, var(--white) 0%, var(--paper) 100%);
    color: var(--ink);
  }
  .front-brand { position: absolute; left: 36px; top: 28px; }
  .front-brand .brand-tagline { font-size: 9px; }
  .divider {
    position: absolute; left: 0; right: 0; top: 102px;
    height: 1.5px; background: var(--ink);
  }
  .contacts {
    position: absolute; left: 36px; top: 122px;
    list-style: none;
    font-size: 15px; line-height: 26px;
  }
  .contacts li { display: flex; align-items: center; gap: 10px; }
  .contacts svg { width: 16px; height: 16px; fill: var(--red); flex: none; }
  .person { position: absolute; right: 34px; top: 200px; text-align: right; }
  .person-name { font-size: 24px; font-weight: 600; line-height: 1.1; }
  .person-name .surname { color: var(--red); }
  .person-title { font-size: 15px; margin-top: 2px; }
  .address {
    position: absolute; right: 34px; bottom: 14px;
    text-align: right; font-size: 14px; line-height: 1.3; font-style: normal;
  }
</style>
</head>
<body>

<section class="card card--back" aria-label="Business card back">
  <div class="back-brand">
    <div class="brand-name"><span class="brand-mark"></span>Brightvane Contracting</div>
    <div class="brand-tagline">Providing Effective Project Controls and Management Solutions</div>
  </div>
  <div class="web-band">
    <span class="web">www.brightvanecontracting.com.au</span>
  </div>
  <div class="sectors">
    <div class="sectors-heading">SUPPORTING CLIENTS IN</div>
    <div>Oil &amp; Gas | Minerals &amp; Metals | Petrochemical | Manufacturing</div>
    <div>Building &amp; Construction | Telecommunication | Rail | Civil | New Industries</div>
    <div class="capabilities">KNOWLEDGE | EXPERTISE | EXPERIENCE | CAPACITY</div>
  </div>
</section>

<section class="card card--front" aria-label="Business card front">
  <div class="front-brand">
    <div class="brand-name"><span class="brand-mark"></span>Brightvane Contracting</div>
    <div class="brand-tagline">Providing Effective Project Controls and Management Solutions</div>
  </div>
  <div class="divider"></div>

  <ul class="contacts">
    <li>
      <svg viewBox="0 0 16 16" aria-hidden="true"><path d="M4 1h3l1 4-2 1.5a9 9 0 0 0 3.5 3.5L11 8l4 1v3a2 2 0 0 1-2 2A12 12 0 0 1 2 3a2 2 0 0 1 2-2z"/></svg>
      +61 0497365128
    </li>
    <li>
      <svg viewBox="0 0 16 16" aria-hidden="true"><path d="M4 1h8v4H4zM1 6h14v6h-3v3H4v-3H1zM5 10v4h6v-4z"/></svg>
      +61 0497365129
    </li>
    <li>
      <svg viewBox="0 0 16 16" aria-hidden="true"><path d="M1 3h14v10H1zM2.5 4.5 8 9l5.5-4.5v-.1H2.5z"/></svg>
      marcusfeld@brightvanecontracting.com.au
    </li>
    <li>
      <svg viewBox="0 0 16 16" aria-hidden="true"><path d="M8 1a7 7 0 1 0 0 14A7 7 0 0 0 8 1zm0 1.5c.8 0 1.8 1.6 2.1 4H5.9C6.2 4.1 7.2 2.5 8 2.5zM5.9 9.5h4.2c-.3 2.4-1.3 4-2.1 4s-1.8-1.6-2.1-4zM2.6 6.5a5.6 5.6 0 0 1 2.5-3.3 8 8 0 0 0-.7 3.3zm0 3h1.8a8 8 0 0 0 .7 3.3 5.6 5.6 0 0 1-2.5-3.3zm10.8-3h-1.8a8 8 0 0 0-.7-3.3 5.6 5.6 0 0 1 2.5 3.3zm0 3a5.6 5.6 0 0 1-2.5 3.3 8 8 0 0 0 .7-3.3z"/></svg>
      www.brightvanecontracting.com.au
    </li>
  </ul>

  <div class="person">
    <div class="person-name">Marcus <span class="surname">Feld</span></div>
    <div class="person-title">Director</div>
  </div>

  <address class="address">
    14 Harbour Lane<br>
    Perth, WA 6000
  </address>
</section>

</body>
</html>
```